Business Card Design Project

We need a business card design for a new company based in Singapore called 'Bright Harbor Pte Ltd'. We provide personal development training and emotional intelligence workshops. Our slogan is "Actualize your potentials". We will not have a company address on the business card. Only phone number, email address and website address.

Target Market(s)

Adults age 25 to 45 years old.
Mostly working in a job.

Industry/Entity Type

Training

Colors
0255a2
f37123

```html
<!DOCTYPE html>
<html lang="en">
<head>
<meta charset="utf-8">
<title>Bright Harbor Pte Ltd – Business Card</title>
<link rel="stylesheet" href="https://fonts.googleapis.com/css2?family=Open+Sans:wght@400;600;700&display=swap">
<style>
  :root {
    --page-bg: #e4e6e9;
    --card-white: #ffffff;
    --soft-white: #eef0f2;
    --crescent-grey: #9a9b9d;
    --brand-blue: #0255a2;
    --brand-orange: #f37123;
    --blue-deep: #2456b8;
    --blue-light: #0a9ae6;
    --ink-white: #ffffff;
  }
  * { margin: 0; padding: 0; box-sizing: border-box; }
  html, body {
    width: 1200px;
    height: 865px;
    overflow: hidden;
    background: var(--page-bg);
    font-family: "Open Sans", Arial, sans-serif;
  }
  .business-card {
    position: absolute;
    left: 100px;
    top: 147px;
    width: 1000px;
    height: 571px;
    overflow: hidden;
    box-shadow: 0 14px 40px rgba(0, 0, 0, 0.18);
  }
  .card-shapes {
    position: absolute;
    inset: 0;
    width: 100%;
    height: 100%;
  }
  .brand-block {
    position: absolute;
    left: 90px;
    top: 290px;
  }
  .brand-mark {
    display: flex;
    align-items: center;
    gap: 14px;
  }
  .brand-dot {
    width: 24px;
    height: 24px;
    border-radius: 50%;
    background: var(--brand-orange);
  }
  .brand-name {
    font-size: 36px;
    font-weight: 600;
    color: var(--brand-blue);
    letter-spacing: 1px;
    white-space: nowrap;
  }
  .slogan {
    margin-top: 6px;
    margin-left: 38px;
    font-size: 17px;
    font-weight: 400;
    font-style: italic;
    color: var(--brand-orange);
    letter-spacing: 0.5px;
  }
  .contact-block {
    position: absolute;
    right: 50px;
    top: 70px;
    text-align: right;
    color: var(--ink-white);
  }
  .person-name {
    font-size: 25px;
    font-weight: 700;
    line-height: 1.2;
  }
  .person-role {
    font-size: 22px;
    font-weight: 400;
    line-height: 1.25;
  }
  .contact-lines {
    margin-top: 70px;
    font-size: 20px;
    line-height: 1.45;
  }
  .contact-line {
    display: flex;
    justify-content: flex-end;
    align-items: center;
    gap: 8px;
  }
  .contact-line svg { width: 18px; height: 18px; fill: var(--ink-white); }
  .web-line {
    margin-top: 14px;
    font-size: 20px;
    line-height: 1.45;
  }
</style>
</head>
<body>
  <div class="business-card">
    <svg class="card-shapes" viewBox="0 0 1000 571" preserveAspectRatio="none" aria-hidden="true">
      <defs>
        <radialGradient id="blueField" cx="0.68" cy="0.5" r="0.6">
          <stop offset="0" stop-color="#0a9ae6"/>
          <stop offset="1" stop-color="#2456b8"/>
        </radialGradient>
        <radialGradient id="whiteField" cx="0.4" cy="0.35" r="0.7">
          <stop offset="0" stop-color="#ffffff"/>
          <stop offset="1" stop-color="#eef0f2"/>
        </radialGradient>
      </defs>
      <rect class="blue-field" width="1000" height="571" fill="url(#blueField)"/>
      <path class="white-field" d="M0 0 H370 C600 50 710 250 645 410 C612 480 572 530 532 571 H0 Z" fill="url(#whiteField)"/>
      <path class="grey-crescent" d="M535 150 C640 240 660 400 575 520 L535 571 H470 C575 470 600 300 535 150 Z" fill="var(--crescent-grey)"/>
    </svg>

    <div class="brand-block">
      <div class="brand-mark">
        <span class="brand-dot"></span>
        <span class="brand-name">BRIGHT HARBOR</span>
      </div>
      <p class="slogan">Actualize your potentials</p>
    </div>

    <div class="contact-block">
      <p class="person-name">Maren Ellery-Voss</p>
      <p class="person-role">Consultant</p>

      <div class="contact-lines">
        <p class="contact-line">065 812 4470
          <svg viewBox="0 0 24 24" aria-label="Phone"><path d="M6.6 10.8c1.4 2.8 3.8 5.1 6.6 6.6l2.2-2.2c.3-.3.7-.4 1-.2 1.1.4 2.3.6 3.6.6.6 0 1 .4 1 1V20c0 .6-.4 1-1 1C10.6 21 3 13.4 3 4c0-.6.4-1 1-1h3.5c.6 0 1 .4 1 1 0 1.3.2 2.5.6 3.6.1.3 0 .7-.2 1z"/></svg>
        </p>
        <p class="contact-line">065 812 4471
          <svg viewBox="0 0 24 24" aria-label="Fax"><path d="M6 2h9l3 3v5H6zM3 11h18v10H3zm3 3v2h3v-2zm5 0v2h3v-2zm5 0v2h2v-2zM6 18v1h3v-1zm5 0v1h3v-1z"/></svg>
        </p>
        <p class="contact-line">hello@brightharbor.sg
          <svg viewBox="0 0 24 24" aria-label="Email"><path d="M2 5h20v14H2zm2 2v.5l8 5.5 8-5.5V7zm0 2.9V17h16V9.9l-8 5.5z"/></svg>
        </p>
      </div>

      <p class="web-line">www.brightharbor.sg</p>
    </div>
  </div>
</body>
</html>
```